The Maplewood Family Clinic needs a Letterhead

We are a bilingual pediatric clinic located in Montreal, Canada.

Our english name is Maplewood Family Clinic
Our french name is Clinique du parc Verdelle

We offer complete care for children including general pediatric care, pediatric specialist care such as Ear, Nose and Throat, Urology, Neurology and Adolescent Medicine. We also have paramedical specialists such as psychologists, social workers, occupational therapists, speech and language pathologists.

The letterhead must use and be harmonious with our new logo. See Design #7150846. We need two types of letterhead. One for a the Logo and both english and french names on the top and the second with the list of current staff on the left. I have uploaded two old examples for you to see. Thanks and good luck.

Industry/Entity Type

Clinic

Font styles to use
Sans Serif

Colors
3176b5
9d9d9d

Requirements
Must have
• Include our logo.
Nice to have
• Most of our printing is done in black and white. So a grayscale design is fine.
I have included a color and grayscale versions of our logo.

We prefer clean modern designs.

```html
<!DOCTYPE html>
<html lang="en">
<head>
<meta charset="utf-8">
<title>Maplewood Family Clinic — Letterheads</title>
<link href="https://fonts.googleapis.com/css2?family=Roboto:wght@300;400;700&display=swap" rel="stylesheet">
<style>
  :root {
    --backdrop: #e6e7e9;
    --paper: #ffffff;
    --frame: #3176b5;
    --brand: #6270b5;
    --ink: #4a5a9a;
    --staff-ink: #3b4f8c;
    --watermark: #eff0f6;
  }
  * { box-sizing: border-box; margin: 0; padding: 0; }
  html, body { width: 1200px; height: 900px; overflow: hidden; }
  body {
    background: var(--backdrop);
    font-family: "Roboto", Arial, sans-serif;
    position: relative;
  }
  .sheet {
    position: absolute;
    top: 156px;
    width: 416px;
    height: 588px;
    background: var(--paper);
    overflow: hidden;
  }
  .sheet--staff { left: 146px; }
  .sheet--plain { left: 608px; }
  .sheet__frame {
    position: absolute;
    inset: 6px;
    border: 1px solid var(--frame);
  }
  .sheet__watermark {
    position: absolute;
    left: 27px;
    top: 131px;
    width: 362px;
    height: 328px;
    border-radius: 50%;
    background: var(--watermark);
  }
  .brand {
    position: absolute;
    top: 28px;
    display: flex;
    align-items: center;
    gap: 6px;
    color: var(--brand);
    font-weight: 300;
    font-size: 11.5px;
    line-height: 12.5px;
  }
  .sheet--staff .brand { left: 30px; }
  .sheet--plain .brand { right: 18px; }
  .brand__fr { text-align: center; }
  .brand__en { text-align: center; }
  .brand__dot {
    width: 42px;
    height: 42px;
    border-radius: 50%;
    background: var(--brand);
  }
  .staff {
    position: absolute;
    top: 96px;
    right: 302px;
    text-align: right;
    color: var(--staff-ink);
    font-size: 4.6px;
    line-height: 6.2px;
  }
  .staff__group { margin-bottom: 8px; }
  .staff__role { font-weight: 700; }
  .staff__icon { display: inline-block; width: 5px; height: 4px; background: var(--staff-ink); vertical-align: middle; margin-left: 2px; }
  .footer {
    position: absolute;
    left: 0; right: 0;
    top: 554px;
    text-align: center;
    color: var(--ink);
    font-size: 7.6px;
    line-height: 9.8px;
    font-weight: 400;
  }
  .sheet--staff .footer { font-weight: 300; letter-spacing: 0.2px; }
</style>
</head>
<body>

<section class="sheet sheet--staff">
  <div class="sheet__watermark" role="img" aria-label="Faint clinic emblem in the background"></div>
  <div class="sheet__frame"></div>
  <header class="brand">
    <div class="brand__fr">Clinique<br>du parc<br>Verdelle</div>
    <div class="brand__dot"></div>
    <div class="brand__en">Maplewood<br>Family<br>Clinic</div>
  </header>
  <aside class="staff">
    <div class="staff__group">
      <div class="staff__role">Adresse / Address</div>
      2280 boul. Verdelle<br>Suite 100<br>Pointe-Claire, Qc<br>H9R 3K2
    </div>
    <div class="staff__group">
      (514) 555-0142 <span class="staff__icon"></span><br>
      (514) 555-0199 <span class="staff__icon"></span>
    </div>
    <div class="staff__group">
      <div class="staff__role">Pédiatres / Pediatricians</div>
      H. Morin<br>J. Talbot<br>R. Lindqvist<br>D. Carter<br>N. Gagnon<br>M. Fontaine<br>D. Becker
    </div>
    <div class="staff__group">
      <div class="staff__role">Neurologue / Neurologist</div>
      M. Arnaud
    </div>
    <div class="staff__group">
      <div class="staff__role">O.R.L. / E.N.T.</div>
      T. Haddad
    </div>
    <div class="staff__group">
      <div class="staff__role">Urologue / Urologist</div>
      R. Novak
    </div>
    <div class="staff__group">
      <div class="staff__role">Psychologues / Psychologists</div>
      H. Pelletier<br>A. Roy
    </div>
    <div class="staff__group">
      <div class="staff__role">Travailleuse social / Social worker</div>
      S. Dubois
    </div>
    <div class="staff__group">
      <div class="staff__role">Diététiste / Dietician</div>
      L. Rinaldi
    </div>
    <div class="staff__group">
      <div class="staff__role">Gérante / Manager</div>
      C. Lemieux
    </div>
  </aside>
  <footer class="footer">
    2280 boul. Verdelle, Suite 100, Pointe-Claire, Qc, H9R 3K2<br>
    tél (514) 555-0142 fax (514) 555-0199
  </footer>
</section>

<section class="sheet sheet--plain">
  <div class="sheet__watermark" role="img" aria-label="Faint clinic emblem in the background"></div>
  <div class="sheet__frame"></div>
  <header class="brand">
    <div class="brand__fr">Clinique<br>du parc<br>Verdelle</div>
    <div class="brand__dot"></div>
    <div class="brand__en">Maplewood<br>Family<br>Clinic</div>
  </header>
  <footer class="footer">
    2280 boul. Verdelle, Suite 100, Pointe-Claire, Qc, H9R 3K2<br>
    tel (514) 555-0142 fax (514) 555-0199
  </footer>
</section>

</body>
</html>
```